Website for Law Firm in California with Existing Logo (Pagewright)

I need a website for a law firm based in Orange County, California, called "Hollis Legal Group." The firm will provide civil litigation and business advice services. The principal practice areas include business litigation, real estate litigation, construction litigation, and other general commercial litigation.

I practiced at a very large, international law firm for 10 years (Merrow Tash LLP) before starting Hollis Legal Group.

At the moment, Hollis Legal Group has one attorney, Corwin J. Hollis (me).

I have a logo for Hollis Legal Group (see attached files, including vectors and transparent background)--which is dark blue and gray. I am open to color changes/tweaks, but would prefer designs that communicate dependability, competence, sophistication, and trustworthiness.

The site should include a home page, as well as separate pages containing: (1) information about the firm and Corwin Hollis (e.g., "About"); (2) information about the firm's practice areas (use "Practice Areas"); (3) a "Contact Us" page where the visitor can insert contact information and describe their legal problem or help sought; (4) a page for articles and blog posts.

I'd also like to mention the practice areas on the main page with links to pages dedicated to each practice area. My thought is that these "practice areas" pages will have a similar look and design, but I will, of course, alter the content for each one.

The practice areas to list for now (I may add more or remove some later are):

Business Litigation
Real Estate Litigation
Banking & Lending Litigation
Contract Disputes
Construction Litigation
Commercial Litigation
Fraud Claims
Breach of Fiduciary Claims
Creditor's Rights
Judgment Collection
Appellate Law
Consumer and Personal Injury Claims
ADA Disputes
Other Civil Litigation
General Corporate Advice
Contract Review
Business Entity Formation

Each page should include easily viewable contact information without appearing cheesy.

I uploaded some head shots and photos of my building as well. They need not all be used. Feel free to play with adjustments to the photos (B&W, contrast, etc.).

I own and reserve the copyright to all files, logos, and pictures uploaded with this design.

I will provide a description of the firm and Corwin Hollis for the about page, as well as a summary of each practice area for the practice area page.

I will also need the ability to put a small description of the localities served by the firm at the bottom of each page on the site, along with a website disclaimer about representations made (I will provide the language for this too).

I am contemplating creating additional websites for different practice areas as well. So this may grow into a larger project if your design is selected. I will likely want to link to those sites from my home site if it makes sense to do so.

Thank you.

Reason: I was involved in a car incident yesterday and need a few more days to review designs. Thanks.

Target Market(s)

Legal Services for businesses and business owners, also individuals.

Industry/Entity Type

Attorney

Contact Information for Business Card

Please include my name and the title "Managing Attorney." Please include fields for my address, telephone number, and email address. Also please include "Orange County" and "Los Angeles" on the card.

Font styles to use
Sans Serif

Requirements
Must have
• See description
Nice to have
• See description
Should not have
• See description

```html
<!DOCTYPE html>
<html lang="en">
<head>
<meta charset="utf-8">
<title>Hollis Legal Group — Home Page Concepts</title>
<link rel="stylesheet" href="https://fonts.googleapis.com/css2?family=Cinzel:wght@400;600&family=Montserrat:wght@400;500&family=Dancing+Script:wght@600&display=swap">
<style>
  :root {
    --navy: #0d2c79;
    --navy-deep: #0a2466;
    --bar-grey: #9b9b9b;
    --tile-grey: #c9c9c5;
    --ink: #1a1a1a;
    --muted: #8a8a8a;
    --white: #ffffff;
    --canvas: #ffffff;
  }
  * { box-sizing: border-box; margin: 0; padding: 0; }
  html, body { width: 1200px; height: 848px; overflow: hidden; background: var(--canvas); }
  body { position: relative; font-family: "Cinzel", serif; color: var(--ink); }

  .page {
    position: absolute; top: 52px; width: 488px; height: 740px;
    background: var(--white);
    box-shadow: 2px 3px 6px rgba(0,0,0,.35);
    overflow: hidden;
  }
  .page--photo-tiles { left: 95px; }
  .page--grey-tiles { left: 605px; }

  /* Header */
  .site-nav {
    position: absolute; left: 0; top: 0; width: 100%; height: 40px;
    background: var(--navy);
    display: flex; align-items: center; justify-content: space-between;
    padding: 0 14px 0 22px;
  }
  .brand { color: var(--white); font-family: "Cinzel", serif; font-weight: 400; font-size: 13px; letter-spacing: .5px; }
  .nav-links { display: flex; gap: 22px; list-style: none; }
  .nav-links li { color: var(--white); font-size: 7.5px; letter-spacing: .4px; }

  .contact-strip {
    position: absolute; left: 0; top: 40px; width: 100%; height: 17px;
    background: var(--bar-grey);
    display: flex; align-items: center; justify-content: flex-end; gap: 5px;
    padding-right: 16px; color: #e8e8e8;
  }
  .contact-strip .address { font-family: "Montserrat", sans-serif; font-size: 6px; letter-spacing: .3px; }
  .contact-strip .call { font-family: "Dancing Script", cursive; font-size: 9px; color: var(--white); }
  .contact-strip .phone { font-family: "Montserrat", sans-serif; font-weight: 500; font-size: 6.5px; color: var(--white); }

  /* Hero */
  .hero { position: absolute; left: 0; top: 57px; width: 100%; height: 329px; }
  .hero-photo { position: absolute; inset: 0; }
  .page--photo-tiles .hero-photo {
    background: linear-gradient(180deg, #6f93b8 0%, #a8b6c2 30%, #b9bfc2 55%, #d8d6cc 72%, #7f9a5a 85%, #4d6e33 100%);
  }
  .page--grey-tiles .hero-photo {
    background: linear-gradient(200deg, #7fb2ea 0%, #3f86d4 40%, #2a6cc2 75%, #3b7ccc 100%);
  }
  .hero-mark {
    position: absolute; left: 103px; top: 81px; width: 300px; height: 104px;
    border: 3px solid var(--white);
    background: rgba(255,255,255,.62);
    display: flex; flex-direction: column; align-items: center; justify-content: center;
    color: var(--navy); font-family: "Cinzel", serif; font-weight: 400;
    font-size: 30px; line-height: 1.05; letter-spacing: 1px;
  }
  .hero-tagline {
    position: absolute; left: 103px; top: 196px; width: 300px; text-align: center;
    color: var(--white); font-size: 9px; line-height: 11px; letter-spacing: .3px;
    text-shadow: 0 0 3px rgba(0,0,0,.45);
  }
  .hero-location {
    position: absolute; left: 103px; top: 222px; width: 300px; text-align: center;
    color: var(--white); font-size: 6.5px; letter-spacing: .4px;
    text-shadow: 0 0 3px rgba(0,0,0,.45);
  }

  /* Practice areas */
  .practice-title {
    position: absolute; left: 0; top: 410px; width: 100%; text-align: center;
    color: var(--navy); font-size: 18px; font-weight: 400; letter-spacing: .5px;
  }
  .practice-sub {
    position: absolute; left: 0; top: 434px; width: 100%; text-align: center;
    font-family: "Montserrat", sans-serif; font-size: 6.5px; color: var(--muted);
  }
  .practice-grid {
    position: absolute; left: 50px; top: 463px; width: 387px;
    display: grid; grid-template-columns: 126px 130px 127px; grid-template-rows: 86px 86px;
  }
  .page--photo-tiles .practice-grid { column-gap: 2px; row-gap: 4px; }
  .tile { width: 100%; height: 100%; }
  .tile--text {
    display: flex; flex-direction: column; justify-content: center; align-items: center;
    list-style: none; text-align: center; font-size: 6.6px; line-height: 11px; color: var(--ink);
  }
  .page--grey-tiles .tile--text { background: var(--tile-grey); }
  .tile--signing { background: linear-gradient(135deg, #6a84a6 0%, #3a4455 50%, #d8d8d8 100%); }
  .tile--document { background: linear-gradient(135deg, #8c7a6c 0%, #c9c3bb 45%, #e6e2dc 100%); }
  .tile--house { background: linear-gradient(180deg, #9fc3e6 0%, #b99a80 50%, #5f8a3a 100%); }

  /* Footer */
  .site-footer {
    position: absolute; left: 0; top: 666px; width: 100%; height: 74px;
    background: var(--navy-deep);
    display: flex; align-items: center; justify-content: center; gap: 20px; padding-top: 4px;
  }
  .site-footer .brand { font-size: 12px; }
  .footer-links { color: var(--white); font-size: 7.5px; letter-spacing: .3px; }
</style>
</head>
<body>

  <!-- Concept A: photo tiles on white -->
  <section class="page page--photo-tiles">
    <header class="site-nav">
      <span class="brand">HOLLIS LEGAL GROUP</span>
      <ul class="nav-links"><li>Home</li><li>About</li><li>Practice Areas</li><li>Contact Us</li></ul>
    </header>
    <div class="contact-strip">
      <span class="address">ADDRESS DETAILS |</span><span class="call">Call us today</span><span class="phone">000-000-000</span>
    </div>
    <div class="hero">
      <div class="hero-photo" role="img" aria-label="Office building entrance with palm trees and landscaped planters"></div>
      <div class="hero-mark"><span>HOLLIS</span><span>LEGAL GROUP</span></div>
      <p class="hero-tagline">Providing civil litigation<br>and business advice services</p>
      <p class="hero-location">ORANGE COUNTY | CALIFORNIA</p>
    </div>
    <h2 class="practice-title">PRACTICE AREAS</h2>
    <p class="practice-sub">Sub heading here introducing practice areas</p>
    <div class="practice-grid">
      <div class="tile tile--signing" role="img" aria-label="Hands signing a document at a desk"></div>
      <ul class="tile tile--text"><li>Business Litigation</li><li>Real Estate Litigation</li><li>Banking &amp; Lending Litigation</li><li>Contract Disputes</li><li>Construction Litigation</li><li>Commercial Litigation</li></ul>
      <div class="tile tile--document" role="img" aria-label="Hand holding a pen over a contract"></div>
      <ul class="tile tile--text"><li>Fraud Claims</li><li>Breach of Fiduciary Claims</li><li>Creditor's Rights</li><li>Judgment Collection</li><li>Appellate Law</li><li>Consumer &amp; Personal Injury Claims</li></ul>
      <div class="tile tile--house" role="img" aria-label="Two-storey brick house with front lawn"></div>
      <ul class="tile tile--text"><li>ADA Disputes</li><li>Other Civil Litigation</li><li>General Corporate Advice</li><li>Contract Review</li><li>Business Entity Formation</li></ul>
    </div>
    <footer class="site-footer">
      <span class="brand">HOLLIS LEGAL GROUP</span>
      <span class="footer-links">Footer details | Social media links | Disclaimer</span>
    </footer>
  </section>

  <!-- Concept B: grey text tiles -->
  <section class="page page--grey-tiles">
    <header class="site-nav">
      <span class="brand">HOLLIS LEGAL GROUP</span>
      <ul class="nav-links"><li>Home</li><li>About</li><li>Practice Areas</li><li>Contact Us</li></ul>
    </header>
    <div class="contact-strip">
      <span class="address">ADDRESS DETAILS |</span><span class="call">Call us today</span><span class="phone">000-000-000</span>
    </div>
    <div class="hero">
      <div class="hero-photo" role="img" aria-label="Glass office tower and palm tree against a blue sky"></div>
      <div class="hero-mark"><span>HOLLIS</span><span>LEGAL GROUP</span></div>
      <p class="hero-tagline">Providing civil litigation<br>and business advice services</p>
      <p class="hero-location">ORANGE COUNTY | CALIFORNIA</p>
    </div>
    <h2 class="practice-title">PRACTICE AREAS</h2>
    <p class="practice-sub">Sub heading here introducing practice areas</p>
    <div class="practice-grid">
      <div class="tile tile--signing" role="img" aria-label="Hands signing a document at a desk"></div>
      <ul class="tile tile--text"><li>Business Litigation</li><li>Real Estate Litigation</li><li>Banking &amp; Lending Litigation</li><li>Contract Disputes</li><li>Construction Litigation</li><li>Commercial Litigation</li></ul>
      <div class="tile tile--document" role="img" aria-label="Hand holding a pen over a contract"></div>
      <ul class="tile tile--text"><li>Fraud Claims</li><li>Breach of Fiduciary Claims</li><li>Creditor's Rights</li><li>Judgment Collection</li><li>Appellate Law</li><li>Consumer &amp; Personal Injury Claims</li></ul>
      <div class="tile tile--house" role="img" aria-label="Two-storey brick house with front lawn"></div>
      <ul class="tile tile--text"><li>ADA Disputes</li><li>Other Civil Litigation</li><li>General Corporate Advice</li><li>Contract Review</li><li>Business Entity Formation</li></ul>
    </div>
    <footer class="site-footer">
      <span class="brand">HOLLIS LEGAL GROUP</span>
      <span class="footer-links">Footer details | Social media links | Disclaimer</span>
    </footer>
  </section>

</body>
</html>
```